Driving School needs brochure for clients charged before the courts with Road Rage

We are a driving school who provides courses to those charged with driving with road rage. This brochure which will be a pdf trifold will be emailed to lawyers, judges and clients. Needs to be extremely professional modern and classy.

Target Market(s)

judges, lawyers

Font styles to use
Serif
Sans Serif

Requirements
Must have
• Please replicate the current Savor the Journey brochure regarding the front page and graphic.
Final design will be a single pdf document with front page of trifold at top and inner at bottom. Should look similar in deign to Caution Keeper (brown brochure) brochure. Not same color. Final panel should be very similar/identical and same as middle panel on outside of trifold (top middle panel) i.e., contact information with phone number, email and website should be similar/identical.
Should not have
• any manufacturer name/logo or image that is obviously linked

```html
<!DOCTYPE html>
<html lang="en">
<head>
<meta charset="utf-8">
<title>Road Rage Course Trifold</title>
<link href="https://fonts.googleapis.com/css2?family=Montserrat:ital,wght@0,400;0,500;0,600;0,700;0,800;1,500;1,700;1,800&display=swap" rel="stylesheet">
<style>
:root{
  --backdrop:#7b7b7b;
  --navy:#1f3a6e;
  --paper:#f4f5f5;
  --white:#ffffff;
  --ink:#1c2536;
  --muted:#4a5568;
  --highlight:#f7e37c;
  --gold:#e5bf3a;
  --tread-tone:#4a4d52;
}
*{box-sizing:border-box;margin:0;padding:0}
html,body{width:1200px;height:2597px;overflow:hidden}
body{background:var(--backdrop);font-family:"Montserrat",Arial,sans-serif;color:var(--ink);position:relative}
.sheet{position:absolute;left:50px;width:1100px;height:850px;display:grid;grid-template-columns:repeat(3,1fr);background:var(--paper);box-shadow:0 10px 30px rgba(0,0,0,.35)}
.sheet--outside{top:298px}
.sheet--inside{top:1448px}
.panel{position:relative;overflow:hidden;height:850px}
.photo{position:absolute;display:block}
.tread{position:absolute;background:var(--tread-tone);opacity:.55}

/* outside left: background */
.about{background:var(--white);padding:38px 34px 0}
.about__title{font-weight:800;font-style:italic;color:var(--navy);font-size:26px;text-align:right;margin-bottom:14px}
.about p{font-size:10.2px;line-height:1.5;color:var(--muted);margin-bottom:9px;font-style:italic}
.about .photo{left:0;right:0;bottom:0;height:240px;background:
  radial-gradient(ellipse 30% 60% at 42% 100%,#d8b23a 0%,rgba(216,178,58,0) 70%),
  linear-gradient(180deg,#a9c3d8 0%,#dfe6ea 30%,#c9c6bd 44%,#5d5f61 62%,#2b2d30 100%)}
.about__corner{position:absolute;left:0;bottom:0;width:170px;height:110px;background:var(--navy);clip-path:polygon(0 0,100% 100%,0 100%)}
.about .tread{left:0;bottom:70px;width:60px;height:14px;transform:rotate(33deg);transform-origin:left}

/* outside middle: contact */
.contact{background:var(--navy)}
.contact__top{position:absolute;left:0;right:0;top:0;height:300px;background:var(--white);clip-path:polygon(0 0,100% 0,100% 70%,0 100%)}
.contact .tread{left:0;top:0;width:30px;height:290px}
.quote{position:absolute;left:63px;top:170px;width:240px;height:240px;border-radius:50%;background:var(--white);display:flex;flex-direction:column;align-items:center;justify-content:center;text-align:center;padding:0 26px}
.quote__mark{font-size:52px;font-weight:800;color:var(--navy);line-height:.6;height:30px}
.quote__text{font-weight:700;font-style:italic;font-size:18px;line-height:1.2;color:var(--ink);margin:6px 0}
.contact__heading{position:absolute;top:500px;left:0;right:0;text-align:center;color:var(--highlight);font-weight:700;font-size:20px}
.contact__list{position:absolute;top:560px;left:0;right:0;list-style:none;text-align:center;color:var(--white)}
.contact__list li{margin-bottom:22px;display:flex;flex-direction:column;align-items:center;gap:8px;font-size:14px}
.contact__list strong{font-weight:700}
.icon-dot{width:26px;height:26px;border-radius:50%;background:var(--gold);display:flex;align-items:center;justify-content:center}

/* outside right: cover */
.cover{background:var(--white)}
.cover .photo{left:0;right:0;top:0;height:340px;background:
  radial-gradient(ellipse 45% 30% at 45% 62%,#e2612a 0%,rgba(226,97,42,0) 75%),
  linear-gradient(180deg,#e8eeec 0%,#b9cacd 35%,#7d8f97 55%,#3b4044 100%)}
.cover__title{position:absolute;top:34px;right:24px;text-align:right;color:var(--navy);line-height:1}
.cover__title h1{font-weight:800;font-size:46px;letter-spacing:.5px}
.cover__title p{font-weight:700;font-size:23px;text-transform:uppercase;margin-top:4px}
.cover__slice{position:absolute;left:0;top:300px;width:100%;height:80px;background:var(--white);clip-path:polygon(0 60%,100% 0,100% 100%,0 100%)}
.cover__band{position:absolute;left:0;top:306px;width:100%;height:44px;background:var(--navy);clip-path:polygon(0 100%,100% 0,100% 14%,0 100%)}
.cover__portrait{position:absolute;left:168px;top:236px;width:170px;height:170px;border-radius:50%;border:6px solid var(--white);box-shadow:0 0 0 3px var(--navy);background:linear-gradient(180deg,#b7c08f 0%,#8c8d78 35%,#5c6670 65%,#2f3a44 100%)}
.cover__lede{position:absolute;top:450px;left:30px;right:30px;text-align:center;font-weight:700;font-size:21px;line-height:1.25;color:var(--ink)}
.brand{position:absolute;top:570px;left:0;right:0;text-align:center;color:var(--navy)}
.brand__name{display:flex;align-items:center;justify-content:center;gap:8px;font-weight:800;font-size:20px}
.brand__mark{width:14px;height:14px;border-radius:50%;background:var(--navy)}
.brand__motto{font-size:12px;font-weight:600;margin-top:6px}
.brand__services{font-size:12.5px;font-weight:600;margin-top:42px;line-height:1.5}
.cover .tread{left:0;right:0;bottom:40px;height:22px}
.cover__corner{position:absolute;right:0;bottom:0;width:100%;height:60px;background:var(--navy);clip-path:polygon(100% 0,100% 100%,0 100%)}

/* inside left: topics */
.topics{background:var(--white);padding:44px 30px 0 34px}
.topics__intro{font-weight:700;font-size:16px;line-height:1.25;color:var(--ink)}
.topics__goal{font-weight:700;font-size:10.5px;color:var(--navy);margin:12px 0 16px;line-height:1.35}
.topics__title{font-weight:700;font-size:17px;color:var(--navy);background:linear-gradient(transparent 50%,var(--highlight) 50%);display:inline-block;padding:0 60px 0 2px}
.topic-group{margin-top:12px}
.topic-group h3{font-weight:700;font-size:13px;color:var(--ink);background:var(--highlight);display:inline-block;padding:2px 40px 2px 6px;margin-bottom:6px}
.checklist{list-style:none}
.checklist li{position:relative;padding-left:24px;font-size:10px;line-height:1.35;color:var(--muted);margin-bottom:6px}
.checklist li::before{content:"";position:absolute;left:0;top:1px;width:13px;height:13px;border-radius:50%;background:var(--navy)}
.checklist li::after{content:"";position:absolute;left:4px;top:4px;width:5px;height:3px;border-left:1.6px solid var(--white);border-bottom:1.6px solid var(--white);transform:rotate(-45deg)}

/* inside middle: strategies */
.strategies{background:var(--navy);padding:44px 30px 0 34px;color:var(--white)}
.strategies h3{color:var(--highlight);font-weight:700;font-size:14px;margin:14px 0 8px}
.strategies h3:first-child{margin-top:0}
.strategies .checklist li{color:#e6ebf4}
.strategies .checklist li::before{background:var(--white)}
.strategies .checklist li::after{border-color:var(--navy)}
.strategies .photo{left:0;right:0;bottom:0;height:230px;background:
  radial-gradient(ellipse 30% 40% at 58% 55%,#e9d6c6 0%,rgba(233,214,198,0) 75%),
  linear-gradient(180deg,#1f3a6e 0%,#3d5378 22%,#7b8594 55%,#c4cad2 100%)}

/* inside right: format */
.format{background:var(--white)}
.format .photo{left:0;right:0;top:0;height:330px;background:
  radial-gradient(ellipse 40% 45% at 45% 45%,#efe4d6 0%,rgba(239,228,214,0) 75%),
  linear-gradient(150deg,#e6c27f 0%,#b99a70 40%,#5d6a73 100%)}
.format__chevron{position:absolute;left:0;top:270px;width:100%;height:90px;background:var(--navy);clip-path:polygon(0 0,45% 70%,100% 0,100% 100%,0 100%)}
.format__chevron-cap{position:absolute;left:0;top:285px;width:100%;height:90px;background:var(--white);clip-path:polygon(0 0,45% 70%,100% 0,100% 100%,0 100%)}
.badge{position:absolute;left:170px;top:185px;width:185px;height:185px;border-radius:50%;background:var(--white);border:5px solid var(--navy);display:flex;align-items:center;justify-content:center;text-align:center;font-weight:700;font-size:17px;line-height:1.2;padding:0 18px}
.format__headline{position:absolute;top:410px;left:34px;line-height:1}
.format__headline span{display:block;font-weight:800;font-size:34px;color:var(--ink)}
.format__headline span + span{color:#6a6f66}
.format .illustration{left:40px;right:30px;top:500px;height:230px;background:linear-gradient(135deg,#f3f4f6 0%,#e4e7ec 55%,#f1b9a4 100%)}
.format .tread{right:0;bottom:30px;width:220px;height:20px}
.format__corner{position:absolute;right:0;bottom:0;width:100%;height:70px;background:var(--navy);clip-path:polygon(100% 0,100% 100%,30% 100%)}
</style>
</head>
<body>

<section class="sheet sheet--outside">
  <article class="panel about">
    <h2 class="about__title">Our background:</h2>
    <p>Since its inception in 1998, Lane Wise Driving Academy has strived to help drivers maintain their driving independence while leading safe and productive lives. Our motto "making drivers safe for life" drives our vision of helping drivers across industries and at all stages of their driving careers.</p>
    <p>Lane Wise started out working with school boards to deliver driver training to beginner drivers. Thousands of students have graduated from our ministry-approved curriculum. We are also ministry-approved to instruct defensive driving (DDC) and driver improvement courses (DIC) for drivers with speeding tickets, demerit points and at-fault crashes.</p>
    <p>Lane Wise has also evolved to provide comprehensive driver rehabilitation to those who have lost or are at risk of losing their license for medical reasons. This includes mobility issues requiring adaptive equipment, as well as traumatic crashes resulting in cognitive impairments and PTSD. We work with clients before the courts charged with impaired driving (alcohol, cannabis, opioids), road rage and stunt driving.</p>
    <p>Founder Daniel Hartley started driving at an early age on his parent's farm. Driving professionally and doing so safely is in his DNA. Daniel has a degree in Business and Psychology and is a certified in-car and in-class driving instructor.</p>
    <div class="photo" role="img" aria-label="Photo of an empty two-lane highway with yellow centre lines through a pale landscape"></div>
    <div class="about__corner"></div>
  </article>

  <article class="panel contact">
    <div class="contact__top"></div>
    <div class="tread" role="img" aria-label="Tire tread marks"></div>
    <blockquote class="quote">
      <span class="quote__mark">&ldquo;</span>
      <span class="quote__text">Maintaining driving independence, while leading safe and productive lives!</span>
      <span class="quote__mark">&rdquo;</span>
    </blockquote>
    <h2 class="contact__heading">For more information:</h2>
    <ul class="contact__list">
      <li><span class="icon-dot"><svg width="14" height="14" viewBox="0 0 24 24"><path fill="#1f3a6e" d="M6.6 10.8a15.1 15.1 0 0 0 6.6 6.6l2.2-2.2a1 1 0 0 1 1-.25 11.4 11.4 0 0 0 3.6.57 1 1 0 0 1 1 1V20a1 1 0 0 1-1 1A17 17 0 0 1 3 4a1 1 0 0 1 1-1h3.5a1 1 0 0 1 1 1c0 1.25.2 2.45.57 3.57a1 1 0 0 1-.25 1z"/></svg></span><span><strong>Call:</strong>&nbsp; 555-014-7720</span></li>
      <li><span class="icon-dot"><svg width="14" height="14" viewBox="0 0 24 24"><path fill="none" stroke="#1f3a6e" stroke-width="2.2" d="M3 6h18v12H3zM3 6l9 7 9-7"/></svg></span><span>info@lanewisedriving.ca</span></li>
      <li><span class="icon-dot"><svg width="14" height="14" viewBox="0 0 24 24"><circle cx="12" cy="12" r="9" fill="none" stroke="#1f3a6e" stroke-width="2"/><path fill="none" stroke="#1f3a6e" stroke-width="1.6" d="M3 12h18M12 3c3 3 3 15 0 18M12 3c-3 3-3 15 0 18"/></svg></span><span>www.lanewisedriving.ca</span></li>
    </ul>
  </article>

  <article class="panel cover">
    <div class="photo" role="img" aria-label="Photo of an orange sports car driving on a coastal highway"></div>
    <header class="cover__title">
      <h1>ROAD RAGE</h1>
      <p>Savor the Journey</p>
    </header>
    <div class="cover__slice"></div>
    <div class="cover__band"></div>
    <div class="cover__portrait" role="img" aria-label="Photo of a driving instructor seated beside a student in a car"></div>
    <p class="cover__lede">A 1-day educational course for those charged with Road Rage.</p>
    <div class="brand">
      <div class="brand__name"><span class="brand__mark"></span>Lane Wise Driving Academy</div>
      <p class="brand__motto">Making drivers safe...for life!</p>
      <p class="brand__services">For all your G License needs!<br>Beginner, Rehabilitation &amp; Remedial</p>
    </div>
    <div class="tread" role="img" aria-label="Tire tread marks"></div>
    <div class="cover__corner"></div>
  </article>
</section>

<section class="sheet sheet--inside">
  <article class="panel topics">
    <p class="topics__intro">A 1-day, 7-hour, intensive remedial measures course for those charged with road rage</p>
    <p class="topics__goal">Our goal is to equip our customers with knowledge and to help them avoid something devastating and/or irreversible from happening in the future.</p>
    <h2 class="topics__title">Topics covered:</h2>
    <div class="topic-group">
      <h3>Law:</h3>
      <ul class="checklist">
        <li>Highway Traffic Act (privilege vs right)</li>
        <li>Federal and Provincial</li>
        <li>Implications of criminal record (financial, work, relationships, etc.)</li>
      </ul>
    </div>
    <div class="topic-group">
      <h3>Road Rage:</h3>
      <ul class="checklist">
        <li>Triggers</li>
        <li>Personality types (Type A); Holmes &amp; Rahe stress scale</li>
        <li>Aggressive driving (overlap between aggressors and victims)</li>
        <li>Psychiatric issues/PTSD: Not uncommon to have professional drivers come through the course due to over-exposure to stress from driving (both on the job or the commute to their driving job)</li>
      </ul>
    </div>
    <div class="topic-group">
      <h3>Physiology and the negative impacts of stress on the body</h3>
      <ul class="checklist">
        <li>Fight or flight response: how it works</li>
        <li>Hormones (Adrenaline, Cortisol, etc.)</li>
        <li>Chronic levels of exposure/immune system suppression, hypertension</li>
        <li>Substances (will do brief overview of drinking and driving if relevant i.e., individual risk factors and thresholds)</li>
      </ul>
    </div>
  </article>

  <article class="panel strategies">
    <h3>Strategies to manage:</h3>
    <ul class="checklist">
      <li>Window of tolerance (hyper-arousal vs hypo-arousal)</li>
      <li>Breathing: how to have the cerebral part of the brain making decisions and not "lizard" part of brain</li>
      <li>We look at how our bodies have not kept up from an evolutionary point of view to manage daily stresses and stimuli</li>
      <li>Our habits: approx. 50% of our decisions are made with little to no decision-making process; stages of change theory</li>
    </ul>
    <h3>Personal context:</h3>
    <ul class="checklist">
      <li>Genetics &amp; socialization (role models &amp; predispositions)</li>
      <li>Analysis of triggers leading up to event; what is really causing it, e.g., sometimes it can be systemic such as our commute</li>
    </ul>
    <h3>Defensive Driving skills:</h3>
    <ul class="checklist">
      <li>The golden rule: Following distance</li>
      <li>Defensive stopping (what we should do every time we apply brakes)</li>
      <li>Using your eyes and strategic driving</li>
      <li>Driving in adverse conditions-they exist every time we drive (human, environmental, machine)</li>
    </ul>
    <div class="photo" role="img" aria-label="Photo of a smiling older woman with glasses driving a car"></div>
  </article>

  <article class="panel format">
    <div class="photo" role="img" aria-label="Photo of a smiling senior couple beside an open car door"></div>
    <div class="format__chevron"></div>
    <div class="format__chevron-cap"></div>
    <p class="badge">Courses are individually tailored one&#8209;on&#8209;one.</p>
    <h2 class="format__headline"><span>OFFERED</span><span>REMOTELY!</span></h2>
    <div class="photo illustration" role="img" aria-label="Illustration of people joining an online video class from laptops and screens"></div>
    <div class="tread" role="img" aria-label="Tire tread marks"></div>
    <div class="format__corner"></div>
  </article>
</section>

</body>
</html>
```